Präsentationsvorlagen für Coworking Anbieter
Zielgruppe
Wir sind ein Coworking Anbieter, der auf Basis eines Mitgliedschaftskonzeptes Verträge mit Büroraumnutzern abschließt. Unser Konzept basiert auf 6 verschiedenen Mitgliedschaften,ROSE; AMBER; KOMET; ONYX; KORALL; OBSIDIAN. Diese Mitgliedschaften möchten wir gerne in einer Präsentation, die wir als PDF per Email versenden vorstellen. Gerne kann die Präsentation auch interaktiv sein.
Aufgabenstellung
Jede Mitgliedschaft soll eine eigene Seite haben in der wir die Details vorstellen. Wobei AMBER und KOMET auf einer Seite vorgestellt werden können, ebenso ONYX und KORALL. Obsidian würde eine eigene Seite bekommen. Ebenso benötigen wir eine Seite mit unseren Services, wie SCANN Service, Postweiterleitungsservice, Virtual private assistant, Telefonsekretariat, Versandservice. Diese Services können auf einer Seite dargestellt werden, also komplett. Ebenso benötigen wir eine Seite auf der alle Mitgliedschaften und Ihre Funktionen dargestellt werden. Die meisten Informationen findet man auf unserer Webseite www.tannenhofraum.com

```html
<!DOCTYPE html>
<html lang="de">
<head>
<meta charset="utf-8">
<title>Tannenhofraum – PDF-Präsentation A4 quer</title>
<link rel="stylesheet" href="https://fonts.googleapis.com/css2?family=Open+Sans:wght@400;600;700&display=swap">
<style>
:root{
  --blue:#1b9ad7;
  --blue-dark:#1689c2;
  --stage:#f4f4f4;
  --paper:#ffffff;
  --text:#8a8a8a;
  --text-dark:#5e5e5e;
  --row-alt:#f1f5f8;
  --line:#e3e9ee;
}
*{box-sizing:border-box;margin:0;padding:0}
html,body{width:1200px;height:2223px;overflow:hidden}
body{background:var(--stage);font-family:"Open Sans",Arial,sans-serif;position:relative}

.page{position:absolute;left:487px;width:345px;height:244px;background:var(--paper);border:1.5px solid var(--blue);box-shadow:0 4px 18px rgba(0,0,0,.08);overflow:hidden}
.page > *{position:absolute}
.page-logo{right:22px;top:12px;font-size:5.5px;font-weight:600;color:var(--blue);letter-spacing:.1px}
.page-url{left:22px;bottom:9px;font-size:3.6px;color:var(--text)}
.page-num{right:22px;bottom:9px;font-size:3.6px;color:var(--text)}
.page-title{left:22px;top:30px;font-size:17px;line-height:20px;font-weight:700;color:var(--blue)}
.body-copy{font-size:4.3px;line-height:7.3px;color:var(--text);text-align:justify}
.body-copy p + p{margin-top:7px}

/* cover */
.cover-photo{left:0;top:0;width:342px;height:123px;background:linear-gradient(180deg,#f6eddc 0%,#f3e2c2 35%,#e9b87a 70%,#d98f3a 100%)}
.cover-title{left:24px;top:140px;font-size:21px;line-height:25px;font-weight:700;color:var(--blue)}
.cover-url{left:24px;top:214px;font-size:9.5px;color:var(--text)}
.cover-logo{right:24px;top:208px;font-size:7px;font-weight:600;color:var(--blue)}
.contact-badge{left:275px;top:98px;width:58px;height:58px;border-radius:50%;background:var(--blue);color:#fff;text-align:center;transform:rotate(8deg);padding-top:15px}
.contact-badge strong{display:block;font-size:9px;font-weight:600}
.contact-badge span{display:block;font-size:5.5px;margin-top:1px}

/* about */
.about-title{top:31px}
.about-copy{left:22px;top:99px;width:147px}
.about-photo{left:188px;top:34px;width:135px;height:187px;background:linear-gradient(180deg,#f5efe4 0%,#efe0c6 45%,#e7c38f 75%,#dc9a48 100%)}

/* locations */
.location{top:70px;width:70px}
.location-photo{width:70px;height:69px}
.location-name{margin-top:16px;font-size:5px;font-weight:700;color:var(--blue)}
.location-copy{margin-top:2px;font-size:4.3px;line-height:7.2px;color:var(--text);text-align:justify}

/* berlin */
.center-title{left:0;right:0;top:30px;text-align:center;font-size:17px;font-weight:700;color:var(--blue)}
.berlin-photo{left:106px;top:64px;width:134px;height:134px;border-radius:50%;background:radial-gradient(circle at 50% 45%,#f6c46a 0%,#d98f3a 45%,#8b6b52 80%,#c9b7a6 100%)}
.feature{width:70px}
.feature h4{font-size:5px;font-weight:700;color:var(--blue)}
.feature p{margin-top:2px;font-size:4.3px;line-height:7.2px;color:var(--text)}

/* services */
.service{top:78px;width:57px;text-align:center}
.service-tile{width:57px;height:56px;background:var(--blue);display:flex;align-items:center;justify-content:center}
.service-name{margin-top:12px;font-size:5px;font-weight:700;color:var(--blue);white-space:nowrap}
.service-copy{margin-top:2px;font-size:4.2px;line-height:7px;color:var(--text)}

/* membership tables */
.plan-table{border-collapse:collapse;table-layout:fixed;font-size:2.9px;line-height:3.6px;color:var(--text)}
.plan-table th,.plan-table td{padding:0 1.5px;text-align:center;vertical-align:middle}
.plan-table thead th{background:var(--blue);color:#fff;font-size:4.5px;font-weight:700;height:9px;border-left:1px solid #fff}
.plan-table thead th.empty{background:transparent;border:0}
.plan-table tbody th{background:var(--blue);color:#fff;font-weight:700;text-align:left;font-size:3px;border-bottom:1px solid rgba(255,255,255,.35)}
.plan-table tbody tr:nth-child(even) td{background:var(--row-alt)}
.plan-table td{border-bottom:.5px solid var(--line)}
.plan-table .tick{color:var(--blue);font-size:6px;font-weight:700;line-height:6px}
.plan-table .price td{color:var(--blue);font-weight:700;font-size:3.3px}
.plan-table small{display:block;font-weight:400;font-size:2.4px;line-height:2.9px}
.member-title{top:32px}
.member-sub{left:22px;top:63px;font-size:5px;font-weight:700;color:var(--blue)}
.member-copy{left:22px;top:73px;width:131px}
.member-table{left:170px;top:34px;width:153px;height:187px}
.overview-table{left:22px;top:34px;width:301px;height:185px}

/* contact page */
.cta-title{top:30px}
.cta-copy{left:22px;top:88px;width:131px}
.imprint{left:176px;top:88px;width:148px;font-size:4.2px;line-height:6.6px;color:var(--text)}
.imprint p + p{margin-top:6.6px}

/* stage branding */
.brand{position:absolute;left:85px;top:2040px;display:flex;align-items:center;gap:12px}
.brand-mark{width:22px;height:22px;border-radius:50%;background:var(--blue)}
.brand-name{font-size:38px;font-weight:400;color:var(--blue);letter-spacing:-.5px}
.stage-caption{position:absolute;left:85px;top:2158px;font-size:15px;font-weight:600;color:#6d6d6d}
</style>
</head>
<body>

<!-- 1 Cover -->
<section class="page" style="top:37px">
  <div class="cover-photo" role="img" aria-label="Foto eines hellen, offenen Büros mit Holzboden und Glaswänden"></div>
  <div class="contact-badge"><strong>Kontakt</strong><span>0221 / 480312-00</span></div>
  <h1 class="cover-title">Büros, Coworking &amp;<br>Geschäftsadresse</h1>
  <div class="cover-url">www.tannenhofraum.com</div>
  <div class="cover-logo">Tannenhofraum</div>
</section>

<!-- 2 About -->
<section class="page" style="top:308px">
  <div class="page-logo">Tannenhofraum</div>
  <h2 class="page-title about-title">Über den<br>Tannenhofraum</h2>
  <div class="body-copy about-copy">
    <p>Als neues Unternehmen im Bereich Co-Working und Business Center verfügt unser Team dennoch über lange Erfahrung und zahlreiche Erfolgsgeschichten zurück. Unsere Mission besteht darin, Büroraum effizient und günstig nutzbar sowie zugänglich zu machen. Mit unserem Membership Konzept können User direkt durchstarten. Dabei behalten sie die notwendige Flexibilität.</p>
    <p>Alle unsere Standorte befinden sich in idealer Lage für dein Geschäft. Wir achten sehr darauf, dass du verkehrsgünstig zu deinem neuen Büro kommen kannst. Dabei ist es egal ob mit dem Auto oder mit öffentlichen Verkehrsmitteln. Fühle dich in unseren Center wohler als in einem anderen Büro. Unsere Lounge versorgt dich kostenfrei mit Kaffee, Wasser, Cappuccino und Tee.</p>
  </div>
  <div class="about-photo" role="img" aria-label="Foto einer Lounge mit weißen Sofas und Holzlamellen"></div>
  <div class="page-url">www.tannenhofraum.com</div><div class="page-num">2</div>
</section>

<!-- 3 Locations -->
<section class="page" style="top:578px">
  <div class="page-logo">Tannenhofraum</div>
  <h2 class="page-title" style="top:32px">Standorte</h2>
  <div class="location" style="left:22px">
    <div class="location-photo" role="img" aria-label="Foto eines modernen weißen Bürogebäudes in Monheim am Rhein" style="background:linear-gradient(180deg,#dfe9f2 0%,#c9ccce 55%,#7f8a6e 100%)"></div>
    <div class="location-name">Monheim am Rhein</div>
    <p class="location-copy">Lorem ipsum dolor sit amet, consetetur sadipscing elitr, sed diam nonumy eirmod tempor invidunt ut labore et dolore magna aliquyam.</p>
  </div>
  <div class="location" style="left:100px">
    <div class="location-photo" role="img" aria-label="Foto eines gläsernen Bürohauses in Frankfurt am Main" style="background:linear-gradient(180deg,#9fc3e0 0%,#4f86b4 55%,#2f5d86 100%)"></div>
    <div class="location-name">Frankfurt am Main</div>
    <p class="location-copy">Lorem ipsum dolor sit amet, consetetur sadipscing elitr, sed diam nonumy eirmod tempor invidunt ut labore et dolore magna aliquyam.</p>
  </div>
  <div class="location" style="left:177px">
    <div class="location-photo" role="img" aria-label="Foto eines beleuchteten Stadttors in Berlin" style="background:linear-gradient(180deg,#e8d9b8 0%,#e6a94c 55%,#7b5a3a 100%)"></div>
    <div class="location-name">Berlin</div>
    <p class="location-copy">Lorem ipsum dolor sit amet, consetetur sadipscing elitr, sed diam nonumy eirmod tempor invidunt ut labore et dolore magna aliquyam.</p>
  </div>
  <div class="location" style="left:254px">
    <div class="location-photo" role="img" aria-label="Foto eines Denkmals vor einer Sandsteinfassade in Bonn" style="background:linear-gradient(180deg,#d9c9a0 0%,#8b7550 55%,#4b5a40 100%)"></div>
    <div class="location-name">Bonn</div>
    <p class="location-copy">Lorem ipsum dolor sit amet, consetetur sadipscing elitr, sed diam nonumy eirmod tempor invidunt ut labore et dolore magna aliquyam.</p>
  </div>
  <div class="page-url">www.tannenhofraum.com</div><div class="page-num">3</div>
</section>

<!-- 4 Berlin -->
<section class="page" style="top:849px">
  <div class="page-logo">Tannenhofraum</div>
  <h2 class="center-title">Standort Berlin</h2>
  <div class="berlin-photo" role="img" aria-label="Rundes Foto eines Stadttors im Abendlicht"></div>
  <div class="feature" style="left:22px;top:78px"><h4>Lorem ipsum</h4><p>Lorem ipsum dolor sit amet, consetetur sadipscing.</p></div>
  <div class="feature" style="left:22px;top:117px"><h4>Lorem ipsum</h4><p>Lorem ipsum dolor sit amet, consetetur sadipscing.</p></div>
  <div class="feature" style="left:22px;top:153px"><h4>Lorem ipsum</h4><p>Lorem ipsum dolor sit amet, consetetur sadipscing.</p></div>
  <div class="feature" style="left:253px;top:78px"><h4>Lorem ipsum</h4><p>Lorem ipsum dolor sit amet, consetetur sadipscing.</p></div>
  <div class="feature" style="left:253px;top:117px"><h4>Lorem ipsum</h4><p>Lorem ipsum dolor sit amet, consetetur sadipscing.</p></div>
  <div class="feature" style="left:253px;top:153px"><h4>Lorem ipsum</h4><p>Lorem ipsum dolor sit amet, consetetur sadipscing.</p></div>
  <div class="page-url">www.tannenhofraum.com</div><div class="page-num">4</div>
</section>

<!-- 5 Services -->
<section class="page" style="top:1120px">
  <div class="page-logo">Tannenhofraum</div>
  <h2 class="page-title" style="top:32px">Services</h2>
  <div class="service" style="left:22px">
    <div class="service-tile"><svg width="30" height="26" viewBox="0 0 30 26" fill="#fff"><rect x="0" y="8" width="6" height="16" rx="1"/><rect x="8" y="8" width="22" height="16" rx="1"/><rect x="11" y="1" width="14" height="9" fill="none" stroke="#fff" stroke-width="1.6"/><g fill="#1b9ad7"><rect x="11" y="13" width="3" height="2"/><rect x="16" y="13" width="3" height="2"/><rect x="21" y="13" width="3" height="2"/><rect x="11" y="17" width="3" height="2"/><rect x="16" y="17" width="3" height="2"/><rect x="21" y="17" width="3" height="2"/></g></svg></div>
    <div class="service-name">Scannen</div>
    <p class="service-copy">Deine eingehende Post wird von uns gescannt.</p>
  </div>
  <div class="service" style="left:83px">
    <div class="service-tile"><svg width="30" height="30" viewBox="0 0 30 30" fill="none" stroke="#fff" stroke-width="2"><path d="M5 13a10 10 0 0 1 18-5"/><path d="M25 17a10 10 0 0 1-18 5"/><path d="M23 3v5h-5M7 27v-5h5"/><rect x="9" y="11" width="12" height="8"/><path d="M9 11l6 4 6-4"/></svg></div>
    <div class="service-name">Postweiterleitung</div>
    <p class="service-copy">Wir leiten deine Post an eine Adresse deiner Wahl weiter. Preis zzgl. Versandporto.</p>
  </div>
  <div class="service" style="left:144px">
    <div class="service-tile"><svg width="30" height="28" viewBox="0 0 30 28" fill="none" stroke="#fff" stroke-width="2"><path d="M3 4h24v15H13l-6 5v-5H3z"/><path d="M8 10h14M8 14h10"/></svg></div>
    <div class="service-name">Virtual Assistant</div>
    <p class="service-copy">Lorem ipsum dolor sit amet, consetetur sadipscing.</p>
  </div>
  <div class="service" style="left:205px">
    <div class="service-tile"><svg width="24" height="26" viewBox="0 0 24 26" fill="#fff"><path d="M6 1c1-.5 2 0 2.5 1l2 5c.4 1-.2 2-1 2.5l-1.5 1c1 3 3 5.6 5.5 7.5l1.4-1.2c.8-.7 2-.8 2.8 0l3.5 3.5c.7.8.6 2-.2 2.7-2 1.8-4.5 2.4-7 1C7 20 2.5 12.5 2.5 6.5 2.5 4 3.8 2 6 1z"/></svg></div>
    <div class="service-name">Telefonsekretariat</div>
    <p class="service-copy">Lorem ipsum dolor sit amet, consetetur sadipscing.</p>
  </div>
  <div class="service" style="left:266px">
    <div class="service-tile"><svg width="30" height="26" viewBox="0 0 30 26" fill="none" stroke="#fff" stroke-width="2"><path d="M2 10L15 2l13 8v14H2z"/><path d="M2 10l13 9 13-9"/><path d="M2 24l10-8M28 24l-10-8"/><path d="M9 8h12M9 11h12"/></svg></div>
    <div class="service-name">Versand</div>
    <p class="service-copy">Lorem ipsum dolor sit amet, consetetur sadipscing.</p>
  </div>
  <div class="page-url">www.tannenhofraum.com</div><div class="page-num">5</div>
</section>

<!-- 6 Membership AMBER & KOMET -->
<section class="page" style="top:1391px">
  <div class="page-logo">Tannenhofraum</div>
  <h2 class="page-title member-title">Mitgliedschaft</h2>
  <div class="member-sub">AMBER &amp; KOMET</div>
  <div class="body-copy member-copy">
    <p>Lorem ipsum dolor sit amet, consetetur sadipscing elitr, sed diam nonumy eirmod tempor invidunt ut labore et dolore magna aliquyam erat, sed diam voluptua. At vero eos et accusam et justo duo dolores et ea rebum. Stet clita kasd gubergren, no sea takimata sanctus est Lorem ipsum dolor sit amet.</p>
    <p>Lorem ipsum dolor sit amet, consetetur sadipscing elitr, sed diam nonumy eirmod tempor invidunt ut labore et dolore magna aliquyam erat, sed diam voluptua. At vero eos et accusam et justo duo dolores et ea rebum. Stet clita kasd gubergren, no sea takimata sanctus est Lorem ipsum dolor sit amet. Lorem ipsum dolor sit amet, consetetur sadipscing elitr, sed diam nonumy eirmod tempor invidunt ut labore et dolore magna aliquyam erat, sed diam voluptua.</p>
  </div>
  <table class="plan-table member-table">
    <colgroup><col style="width:53px"><col><col></colgroup>
    <thead><tr><th class="empty"></th><th>AMBER</th><th>KOMET</th></tr></thead>
    <tbody>
      <tr style="height:22px"><th>Dein Arbeitsplatz</th><td>Flexibler Platz im offenen Coworking-Bereich, frei wählbar nach Verfügbarkeit.</td><td>Flexibler Arbeitsplatz im offenen Bereich, auch im ruhigen Lounge-Bereich nutzbar.</td></tr>
      <tr style="height:11px"><th>24/7 Zugang</th><td>Während der Öffnungszeiten</td><td>Während der Öffnungszeiten</td></tr>
      <tr style="height:15px"><th>inkl. Kontingent</th><td>2 Tage pro Monat inkl., weitere Tage für 9 € je Tag</td><td>5 Tage pro Monat inkl., weitere Tage für 9 € je Tag</td></tr>
      <tr><th>WiFi Flatrate</th><td class="tick">✓</td><td class="tick">✓</td></tr>
      <tr style="height:13px"><th>Getränke Flatrate<small>Kaffee, Cappuccino, Wasser, Tee</small></th><td class="tick">✓</td><td class="tick">✓</td></tr>
      <tr><th>Büroraum Reinigung</th><td class="tick">✓</td><td class="tick">✓</td></tr>
      <tr><th>Nebenkosten inklusive</th><td class="tick">✓</td><td class="tick">✓</td></tr>
      <tr><th>Geschäftsadresse</th><td>Optional für EUR 10,- p.M.</td><td>Optional für EUR 10,- p.M.</td></tr>
      <tr><th>Drucker/Kopierer</th><td class="tick">✓</td><td class="tick">✓</td></tr>
      <tr><th>Scanservice</th><td>Optional für EUR 10,- p.M.</td><td>Optional für EUR 10,- p.M.</td></tr>
      <tr><th>Aktenvernichtungsservice</th><td class="tick">✓</td><td class="tick">✓</td></tr>
      <tr><th>Veranstaltungen</th><td class="tick">✓</td><td class="tick">✓</td></tr>
      <tr><th>Zutritt</th><td>2 Tage p.M.</td><td>5 Tage p.M.</td></tr>
      <tr><th>Postweiterleitung</th><td>Optional für EUR 10,- p.M.</td><td>Optional für EUR 10,- p.M.</td></tr>
      <tr class="price"><th>Preis</th><td>ab 69 € / pro Monat</td><td>ab 149 € / pro Monat</td></tr>
    </tbody>
  </table>
  <div class="page-url">www.tannenhofraum.com</div><div class="page-num">6</div>
</section>

<!-- 7 Overview -->
<section class="page" style="top:1662px">
  <div class="page-logo">Tannenhofraum</div>
  <table class="plan-table overview-table">
    <colgroup><col style="width:53px"><col><col><col><col><col></colgroup>
    <thead><tr><th class="empty"></th><th>AMBER</th><th>KOMET</th><th>ONYX</th><th>KORALL</th><th>OBSIDIAN</th></tr></thead>
    <tbody>
      <tr style="height:21px"><th>Dein Arbeitsplatz</th><td>Flexibler Platz im offenen Coworking-Bereich nach Verfügbarkeit.</td><td>Flexibler Platz, auch im ruhigen Lounge-Bereich nutzbar.</td><td>Fester Schreibtisch im Coworking-Bereich mit eigenem Rollcontainer.</td><td>Fester Arbeitsplatz im Teambüro mit abschließbarem Schrank.</td><td>Eigenes abschließbares Einzelbüro mit voller Ausstattung.</td></tr>
      <tr style="height:11px"><th>24/7 Zugang</th><td>Während der Öffnungszeiten</td><td>Während der Öffnungszeiten</td><td class="tick">✓</td><td class="tick">✓</td><td class="tick">✓</td></tr>
      <tr style="height:15px"><th>inkl. Kontingent</th><td>2 Tage pro Monat inkl., weitere Tage für 9 € je Tag</td><td>5 Tage pro Monat inkl., weitere Tage für 9 € je Tag</td><td>Jeden Tag im Monat, freier Zugang</td><td>Jeden Tag im Monat, freier Zugang</td><td>Jeden Tag im Monat, freier Zugang</td></tr>
      <tr><th>WiFi Flatrate</th><td class="tick">✓</td><td class="tick">✓</td><td class="tick">✓</td><td class="tick">✓</td><td class="tick">✓</td></tr>
      <tr style="height:12px"><th>Getränke Flatrate<small>Kaffee, Cappuccino, Wasser, Tee</small></th><td class="tick">✓</td><td class="tick">✓</td><td class="tick">✓</td><td class="tick">✓</td><td class="tick">✓</td></tr>
      <tr><th>Büroraum Reinigung</th><td class="tick">✓</td><td class="tick">✓</td><td class="tick">✓</td><td class="tick">✓</td><td class="tick">✓</td></tr>
      <tr><th>Nebenkosten inklusive</th><td class="tick">✓</td><td class="tick">✓</td><td class="tick">✓</td><td class="tick">✓</td><td class="tick">✓</td></tr>
      <tr><th>Geschäftsadresse</th><td>Optional für EUR 10,- p.M.</td><td>Optional für EUR 10,- p.M.</td><td>Optional für EUR 10,- p.M.</td><td>Optional für EUR 10,- p.M.</td><td>Optional für EUR 10,- p.M.</td></tr>
      <tr><th>Drucker/Kopierer</th><td class="tick">✓</td><td class="tick">✓</td><td class="tick">✓</td><td class="tick">✓</td><td class="tick">✓</td></tr>
      <tr><th>Scanservice</th><td>Optional für EUR 10,- p.M.</td><td>Optional für EUR 10,- p.M.</td><td>Optional für EUR 10,- p.M.</td><td>Optional für EUR 10,- p.M.</td><td>Optional für EUR 10,- p.M.</td></tr>
      <tr><th>Aktenvernichtungsservice</th><td class="tick">✓</td><td class="tick">✓</td><td class="tick">✓</td><td class="tick">✓</td><td class="tick">✓</td></tr>
      <tr><th>Veranstaltungen</th><td class="tick">✓</td><td class="tick">✓</td><td class="tick">✓</td><td class="tick">✓</td><td class="tick">✓</td></tr>
      <tr><th>Zutritt</th><td>2 Tage p.M.</td><td>5 Tage p.M.</td><td>Unlimited</td><td>Unlimited</td><td>Unlimited</td></tr>
      <tr><th>Postweiterleitung</th><td>Optional für EUR 10,- p.M.</td><td>Optional für EUR 10,- p.M.</td><td>Optional für EUR 10,- p.M.</td><td>Optional für EUR 10,- p.M.</td><td>Optional für EUR 10,- p.M.</td></tr>
      <tr class="price"><th>Preis</th><td>ab 69 € / pro Monat</td><td>ab 149 € / pro Monat</td><td>ab 289 € / pro Monat</td><td>ab 399 € / pro Monat</td><td>ab 699 € / pro Monat</td></tr>
    </tbody>
  </table>
  <div class="page-url">www.tannenhofraum.com</div><div class="page-num">7</div>
</section>

<!-- 8 Contact -->
<section class="page" style="top:1931px">
  <div class="page-logo">Tannenhofraum</div>
  <h2 class="page-title cta-title">Fordern Sie jetzt<br>mehr Infos an</h2>
  <div class="body-copy cta-copy">
    <p>Tur auta eos assitia. Tas nis preperovit eicatibus. Bus ipsunt, antibus aborroratqui renis ma voluptas voluptatat. Obitaque dolores equostr untota verferem que derferchil et id evelluptati cor aliquam etus.</p>
    <p>Cate sam voluptaquodis cendit venes aut et aut et volupta dolupta volorrum facerumtum nis estis mobitatem volo molest andi ilis diorendant pia cuptatemquos aut enda sinullab um vellignatem dolore nihil mossum, ute ad quam inci utatem ipsamet alist, sam aut remperis aut quatur? Qui quatior aliquodit rae dit voloratur, test re, abor sum conecea se nihil eiure, ilicias nes de id unt.</p>
  </div>
  <div class="imprint">
    <p>Lindgrün Arbeitswelt GmbH<br>Ahornweg 12<br>50667 Köln</p>
    <p>Eingetragen im Amtsgericht Köln unter der HRB 40127</p>
    <p>Geschäftsführer: Lea Hartmann<br>Tel.: +49-221-480312-00</p>
    <p>E-Mail: info(at)tannenhofraum.com<br>Web: www.tannenhofraum.com</p>
    <p>Steuernummer: 214/3381/0762</p>
  </div>
  <div class="page-url">www.tannenhofraum.com</div><div class="page-num">8</div>
</section>

<div class="brand"><span class="brand-mark"></span><span class="brand-name">Tannenhofraum</span></div>
<div class="stage-caption">PDF-Präsentation A4 quer - Version 2</div>

</body>
</html>
```